Tarrowby Builders Business Card Design

We require a business Card for a new Building Company called Tarrowby Builders. We are General Builders that specialize in Industrial, Commercial and Domestic building work. We would like to see a design that incorporates Blue ,Red and White as the colour scheme and a design that will highlight a building theme.
(Once this design is achieved will need to incorporate this for the other side of the business which is Tarrowby Joinery )

Contact Information for Business Card

TARROWBY BUILDERS
17 Wendaree Rd Kelverton SA 5362
Mobile 0427390548
Telephone 08 85047316
Marcus Delroy
Director / Supervisor

```html
<!DOCTYPE html>
<html lang="en">
<head>
<meta charset="utf-8">
<title>Tarrowby Builders Business Card</title>
<link rel="stylesheet" href="https://fonts.googleapis.com/css2?family=Open+Sans:ital,wght@0,400;0,600;0,700;1,400&display=swap">
<style>
  :root {
    --royal-blue: #1a1fb8;
    --deep-blue: #0f1290;
    --navy-text: #1c2a8c;
    --accent-red: #e8262d;
    --paper: #ffffff;
    --paper-shade: #ececec;
    --grey-text: #4a4a4a;
    --backdrop: #e4e2de;
  }
  * { box-sizing: border-box; margin: 0; padding: 0; }
  html, body { width: 1200px; height: 843px; overflow: hidden; }
  body {
    background: var(--backdrop);
    font-family: "Open Sans", Arial, sans-serif;
    position: relative;
  }
  .card {
    position: absolute;
    top: 267px;
    width: 540px;
    height: 309px;
    border-radius: 2px;
    box-shadow: 0 6px 18px rgba(0,0,0,0.18);
    overflow: hidden;
  }

  /* Back side */
  .card-back {
    left: 40px;
    background: linear-gradient(135deg, var(--royal-blue) 0%, var(--deep-blue) 100%);
    color: var(--paper);
    display: flex;
    flex-direction: column;
    align-items: center;
    justify-content: center;
    text-align: center;
  }
  .card-back .pattern-area {
    position: absolute; inset: 0;
    background: radial-gradient(ellipse at 60% 30%, rgba(255,255,255,0.12), rgba(255,255,255,0) 60%);
  }
  .back-name {
    position: relative;
    font-weight: 700;
    font-size: 34px;
    letter-spacing: 1px;
    line-height: 1.05;
  }
  .back-tagline {
    position: relative;
    margin-top: 18px;
    font-weight: 700;
    font-size: 15px;
    letter-spacing: 0.5px;
  }
  .back-services {
    position: relative;
    margin-top: 2px;
    font-size: 12.5px;
  }
  .back-services .sep {
    display: inline-block; width: 6px; height: 6px;
    background: var(--paper); margin: 0 5px 2px;
  }

  /* Front side */
  .card-front {
    left: 620px;
    background: linear-gradient(160deg, var(--paper) 55%, var(--paper-shade) 100%);
  }
  .brand {
    position: absolute;
    top: 50px; left: 0; right: 0;
    display: flex; align-items: center; justify-content: center; gap: 12px;
  }
  .brand-square {
    width: 22px; height: 22px; background: var(--accent-red);
  }
  .brand-name {
    font-weight: 700;
    font-size: 30px;
    color: var(--navy-text);
    letter-spacing: 1px;
  }
  .divider {
    position: absolute;
    top: 122px; left: 28px; right: 28px;
    border-top: 1px solid var(--navy-text);
  }
  .divider-contacts {
    position: absolute;
    top: 198px; left: 300px; right: 28px;
    border-top: 1px solid var(--navy-text);
  }
  .person {
    position: absolute;
    top: 134px; left: 30px;
  }
  .person-name {
    font-size: 19px; font-weight: 600; color: var(--navy-text);
  }
  .person-role {
    font-size: 13.5px; font-style: italic; color: var(--accent-red);
    margin-top: 1px;
  }
  .person-address {
    font-size: 13px; color: var(--grey-text); line-height: 1.35; margin-top: 2px;
  }
  .contacts {
    position: absolute;
    right: 26px; bottom: 16px;
    list-style: none;
  }
  .contacts li {
    display: flex; align-items: center; justify-content: flex-end; gap: 10px;
    font-size: 13.5px; color: var(--grey-text); line-height: 20px;
  }
  .contacts svg { width: 13px; height: 13px; fill: var(--navy-text); flex: none; }
</style>
</head>
<body>

<section class="card card-back" aria-label="Business card, back">
  <div class="pattern-area" role="img" aria-label="Faint repeating brand pattern on blue"></div>
  <div class="back-name">TARROWBY<br>BUILDERS</div>
  <div class="back-tagline">GENERAL BUILDERS</div>
  <div class="back-services">Industrial<span class="sep"></span>Commercial<span class="sep"></span>Domestic building work</div>
</section>

<section class="card card-front" aria-label="Business card, front">
  <div class="brand">
    <span class="brand-square"></span>
    <span class="brand-name">TARROWBY BUILDERS</span>
  </div>
  <div class="divider"></div>
  <div class="person">
    <div class="person-name">Marcus Delroy</div>
    <div class="person-role">Director / Supervisor</div>
    <div class="person-address">17 Wendaree Rd<br>Kelverton SA 5362</div>
  </div>
  <div class="divider-contacts"></div>
  <ul class="contacts">
    <li>08 85047316
      <svg viewBox="0 0 24 24"><path d="M6.6 10.8a15.1 15.1 0 0 0 6.6 6.6l2.2-2.2c.3-.3.7-.4 1-.2 1.1.4 2.3.6 3.6.6.6 0 1 .4 1 1V20c0 .6-.4 1-1 1A17 17 0 0 1 3 4c0-.6.4-1 1-1h3.5c.6 0 1 .4 1 1 0 1.3.2 2.5.6 3.6.1.3 0 .7-.2 1z"/></svg></li>
    <li>0427390548
      <svg viewBox="0 0 24 24"><path d="M7 1h10a2 2 0 0 1 2 2v18a2 2 0 0 1-2 2H7a2 2 0 0 1-2-2V3a2 2 0 0 1 2-2zm0 3v14h10V4zm5 15.5a1.2 1.2 0 1 0 0 2.4 1.2 1.2 0 0 0 0-2.4z"/></svg></li>
    <li>office@tarrowbymail.com
      <svg viewBox="0 0 24 24"><path d="M2 5h20v14H2zm2 2v.5l8 5 8-5V7l-8 5z"/></svg></li>
    <li>www.tarrowbysite.com
      <svg viewBox="0 0 24 24"><path d="M12 2a10 10 0 1 0 0 20 10 10 0 0 0 0-20zm6.9 6h-3a15 15 0 0 0-1.3-3.9A8 8 0 0 1 18.9 8zM12 4c.8 1.1 1.5 2.5 1.9 4h-3.8c.4-1.5 1.1-2.9 1.9-4zM4.3 14a8 8 0 0 1 0-4h3.4a16 16 0 0 0 0 4zm.8 2h3a15 15 0 0 0 1.3 3.9A8 8 0 0 1 5.1 16zm3-8h-3a8 8 0 0 1 4.3-3.9A15 15 0 0 0 8.1 8zM12 20c-.8-1.1-1.5-2.5-1.9-4h3.8c-.4 1.5-1.1 2.9-1.9 4zm2.3-6H9.7a14 14 0 0 1 0-4h4.6a14 14 0 0 1 0 4zm.3 5.9a15 15 0 0 0 1.3-3.9h3a8 8 0 0 1-4.3 3.9zm1.7-5.9a16 16 0 0 0 0-4h3.4a8 8 0 0 1 0 4z"/></svg></li>
  </ul>
</section>

</body>
</html>
```